Casino with the 'highest winning percentage' needs a stationery design

This is for a casino in Colombo, Sri Lanka and we need a stationery design for business card, letter head and envelope.

Should be very professional, simple and elegant without fancy fonts

Reason: Not fully satisfied with the designs. Need more designs.

Industry/Entity Type

Business

Requirements
Must have
• 1. card deck symbol 'CLUBS' in red, or black

2. name in BLOCK CAPITAL LETTERS

3. Preferred font colours are black, white or red

4. Prefer 'professional /elegant' fonts
Should not have
• SHOULD NOT HAVE ANY OTHER SYMBOL EXCEPT 'CLUBS'

DO NOT PREFER ITALIC FONTS

```html
<!DOCTYPE html>
<html lang="en">
<head>
<meta charset="utf-8">
<title>Halden's Entertainment – Business Card</title>
<link rel="stylesheet" href="https://fonts.googleapis.com/css2?family=Arimo:wght@400;700&display=swap">
<style>
  :root {
    --backdrop: #e6e7ea;
    --card-white: #fbfbfc;
    --card-black: #2a2a2a;
    --frame-line: #e8e8e8;
    --ink: #1e1e1e;
    --ink-soft: #333333;
    --accent-red: #b0141f;
  }
  * { margin: 0; padding: 0; box-sizing: border-box; }
  html, body {
    width: 1200px;
    height: 934px;
    overflow: hidden;
    background: var(--backdrop);
    font-family: "Arimo", Arial, sans-serif;
  }
  .stationery {
    position: relative;
    width: 1200px;
    height: 934px;
  }
  .card {
    position: absolute;
    top: 317px;
    width: 520px;
    height: 300px;
    border-radius: 2px;
    box-shadow: 0 6px 18px rgba(0, 0, 0, 0.12);
  }
  /* Card back */
  .card-back {
    left: 50px;
    background: var(--card-black);
    padding: 16px;
  }
  .card-back-pattern {
    width: 100%;
    height: 100%;
    border: 2px solid var(--frame-line);
    border-radius: 14px;
    background: radial-gradient(circle at 50% 50%, #3a3a3a 0%, #262626 100%);
  }
  /* Card front */
  .card-front {
    left: 630px;
    background: var(--card-white);
    color: var(--ink);
  }
  .contact {
    position: absolute;
    left: 40px;
    top: 118px;
  }
  .contact-name {
    font-size: 15px;
    font-weight: 700;
    letter-spacing: 0.3px;
    text-transform: uppercase;
  }
  .contact-title {
    margin-top: 5px;
    font-size: 10px;
    color: var(--accent-red);
  }
  .contact-lines {
    margin-top: 14px;
    font-size: 10px;
    line-height: 13px;
    color: var(--ink-soft);
  }
  .contact-lines strong { font-weight: 700; color: var(--ink); }
  .contact-address { margin-top: 11px; }
  .contact-web {
    margin-top: 13px;
    font-size: 10.5px;
    color: var(--ink);
  }
  .brand {
    position: absolute;
    right: 44px;
    top: 62px;
    width: 196px;
    display: flex;
    flex-direction: column;
    align-items: center;
    color: var(--ink);
    font-weight: 400;
  }
  .brand-dot {
    width: 34px;
    height: 34px;
    border-radius: 50%;
    background: var(--accent-red);
    margin-bottom: 12px;
  }
  .brand-name {
    font-size: 30px;
    letter-spacing: 1px;
    line-height: 1;
    text-transform: uppercase;
  }
  .brand-sub {
    margin-top: 6px;
    font-size: 12px;
    letter-spacing: 1.5px;
    text-transform: uppercase;
    padding-bottom: 4px;
    border-bottom: 1px solid var(--ink);
    width: 100%;
    text-align: center;
  }
  .brand-place {
    margin-top: 4px;
    font-size: 8px;
    letter-spacing: 1.5px;
    text-transform: uppercase;
  }
</style>
</head>
<body>
<main class="stationery">
  <section class="card card-back">
    <div class="card-back-pattern" role="img" aria-label="Repeating outlined suit pattern on black inside a thin white rounded frame"></div>
  </section>

  <section class="card card-front">
    <div class="contact">
      <p class="contact-name">Marcus Ellery</p>
      <p class="contact-title">General Manager</p>
      <p class="contact-lines">
        <strong>Tel:</strong> + 94 11 2480716<br>
        <strong>Fax:</strong> + 94 11 2480717
      </p>
      <p class="contact-lines contact-address">
        52, Lotus Grove Road<br>
        Colombo 00300, Sri Lanka
      </p>
      <p class="contact-web">www.<strong>haldenscolombo</strong>.com</p>
    </div>

    <div class="brand">
      <span class="brand-dot"></span>
      <span class="brand-name">Halden's</span>
      <span class="brand-sub">Entertainment</span>
      <span class="brand-place">Sri Lanka</span>
    </div>
  </section>
</main>
</body>
</html>
```